Locksmith Store 474747 Signage

Design Brief: Locksmith Store Signage – "Locksmith 474747" [ΚΛΕΙΔΑΡΑΣ 474747 (in Greek)]
We are looking for a spectacular and professional sign design for the exterior of our locksmith store.
Signage Dimensions:
• Width: 6 meters
• Height: 1.5 meters
• Shopfront window Width: 6 meters, Height: 2.5 meters
Key Requirements (in order of importance):
1. It must be immediately clear that this is a locksmith store. [ΚΛΕΙΔΑΡΑΣ (in Greek)]
2. The store name "474747", (which is also the phone number 2310474747), should be highly visible and visually striking because this is the number that customers are calling when they are locked out.
3. The signage should also clearly communicate that except for house keys, which is obvious for a locksmith store the services we provide are:
o All kinds of house keys. ΚΛΕΙΔΙΑ ΣΠΙΤΙΩΝ(in Greek) (There is no key that we cannot do)
o Immobiliser car keys = ΚΛΕΙΔΙΑ ΑΥΤΟΚΙΝΗΤΩΝ (in Greek)
We unlock every car that exist, we program new immobilizer keys – remote controls, even if all keys are lost, we repair or change broken cells of car keys, we change batteries.
o High-security locks = ΚΛΕΙΔΑΡΙΕΣ ΑΣΦΑΛΕΙΑΣ (in Greek) we sell the best high security locks in the planet
o Armoured doors = ΠΟΡΤΕΣ ΑΣΦΑΛΕΙΑΣ (in Greek) (this may not be so important to be on the signage.
Visual Style:
We are open to creative direction, but the design should be eye-catching, professional, and modern, something that will stand out on a busy street and instantly tell customers who we are and what we offer. Also, you may use the shopfront window for graphic designs. Also, we are open if a part of the signage is digital.
________________________________________
Updates
Hello Designers,
Thank you so much for your effort and the designs you've shared.
I realized I forgot to mention that you can refer to my website at www.474747-keys.example.gr for more context.
Additionally, I’ve just uploaded two new photos: one showing the store with a black outline at the dimensions of the signage, and another with the large double-bit key placed in a different position to demonstrate that it is moveable.
Thanks again for your dedication!
Target Market(s)
every person that has a key
Look and feel
Each slider illustrates characteristics of the customer's brand and the style your logo design should communicate.

```html
<!DOCTYPE html>
<html lang="el">
<head>
<meta charset="utf-8">
<title>ΚΛΕΙΔΑΡΑΣ 474747</title>
<link href="https://fonts.googleapis.com/css2?family=Play:wght@400;700&display=swap" rel="stylesheet">
<style>
  :root {
    --bg-deep: #110f26;
    --bg-mid: #0e1a30;
    --gold-light: #fff1a8;
    --gold: #e3b325;
    --gold-dark: #8a5d08;
    --silver-light: #ffffff;
    --silver: #c9ccd1;
    --silver-dark: #6b6f76;
    --accent-yellow: #f6b414;
    --text-white: #ffffff;
    --ink: #111111;
    --key-tone-a: #9fd11e;
    --key-tone-b: #b9bcc1;
    --door-tone-a: #1b2436;
    --door-tone-b: #9a5a35;
  }
  html, body {
    margin: 0;
    padding: 0;
    overflow: hidden;
    background: var(--bg-deep);
  }
  .sign {
    position: relative;
    width: 1200px;
    height: 300px;
    overflow: hidden;
    background: radial-gradient(ellipse at 55% 40%, var(--bg-mid) 0%, var(--bg-deep) 75%);
    font-family: "Play", sans-serif;
  }
  .key-illustration {
    position: absolute;
    left: 22px;
    top: 8px;
    width: 190px;
    height: 245px;
    border-radius: 30px;
    background: linear-gradient(150deg, var(--key-tone-a) 0%, var(--key-tone-b) 45%, rgba(185,188,193,0.15) 100%);
    opacity: 0.85;
  }
  .door-illustration {
    position: absolute;
    right: 0;
    top: 0;
    width: 180px;
    height: 300px;
    background: linear-gradient(115deg, var(--door-tone-a) 0%, var(--silver-dark) 45%, var(--door-tone-b) 75%);
  }
  .headline {
    position: absolute;
    left: 0;
    top: 0;
    width: 1200px;
    height: 300px;
  }
  .service {
    position: absolute;
    display: flex;
    align-items: center;
    gap: 8px;
    color: var(--accent-yellow);
    font-size: 25px;
    letter-spacing: 1.5px;
    white-space: nowrap;
  }
  .service--left { left: 14px; top: 240px; }
  .service--right { left: 804px; top: 250px; }
</style>
</head>
<body>
<div class="sign">
  <div class="key-illustration" role="img" aria-label="High-security double-bit key with green head"></div>
  <div class="door-illustration" role="img" aria-label="Edge of an armoured door showing lock bolts and a security cylinder"></div>

  <svg class="headline" viewBox="0 0 1200 300" xmlns="http://www.w3.org/2000/svg">
    <defs>
      <linearGradient id="gold-fill" x1="0" y1="0" x2="0" y2="1">
        <stop offset="0" stop-color="var(--gold-light)"/>
        <stop offset="0.45" stop-color="var(--gold)"/>
        <stop offset="0.55" stop-color="var(--gold-dark)"/>
        <stop offset="1" stop-color="var(--gold)"/>
      </linearGradient>
      <linearGradient id="silver-fill" x1="0" y1="0" x2="0" y2="1">
        <stop offset="0" stop-color="var(--silver-light)"/>
        <stop offset="0.5" stop-color="var(--silver)"/>
        <stop offset="0.6" stop-color="var(--silver-dark)"/>
        <stop offset="1" stop-color="var(--silver-light)"/>
      </linearGradient>
    </defs>

    <text class="title" x="189" y="119" textLength="829" lengthAdjust="spacingAndGlyphs"
          font-family="Play, sans-serif" font-weight="700" font-size="100"
          fill="url(#gold-fill)" stroke="var(--gold-dark)" stroke-width="1">ΚΛΕΙΔΑΡΑΣ</text>

    <rect class="rule" x="188" y="161" width="120" height="22" fill="url(#silver-fill)"/>
    <rect class="rule" x="891" y="161" width="127" height="22" fill="url(#silver-fill)"/>

    <rect class="area-code-box" x="316" y="137" width="48" height="70" fill="url(#silver-fill)"/>
    <text class="area-code" transform="translate(350 172) rotate(-90)" text-anchor="middle"
          font-family="Play, sans-serif" font-weight="700" font-size="24" fill="var(--ink)">2310</text>

    <text class="number" x="375" y="204" textLength="507" lengthAdjust="spacingAndGlyphs"
          font-family="Play, sans-serif" font-weight="700" font-size="88"
          fill="url(#silver-fill)" stroke="var(--silver-dark)" stroke-width="1">474747</text>

    <text class="website" x="600" y="247" text-anchor="middle" textLength="440" lengthAdjust="spacingAndGlyphs"
          font-family="Play, sans-serif" font-weight="700" font-size="28" fill="var(--text-white)">www.474747-keys.example.gr</text>
  </svg>

  <div class="service service--left">
    <svg width="52" height="54" viewBox="0 0 52 54" aria-hidden="true">
      <path d="M3 24 L24 6 L45 24" fill="none" stroke="var(--accent-yellow)" stroke-width="4"/>
      <path d="M9 21 V48 H36" fill="none" stroke="var(--accent-yellow)" stroke-width="4"/>
      <circle cx="39" cy="36" r="6" fill="none" stroke="var(--accent-yellow)" stroke-width="3"/>
      <path d="M34 40 L22 52" stroke="var(--accent-yellow)" stroke-width="3"/>
    </svg>
    <span class="service__label">ΚΛΕΙΔΑΡΙΕΣ ΑΣΦΑΛΕΙΑΣ</span>
  </div>

  <div class="service service--right">
    <svg width="44" height="44" viewBox="0 0 44 44" aria-hidden="true">
      <path d="M22 2 L40 8 V22 C40 32 32 39 22 42 C12 39 4 32 4 22 V8 Z" fill="var(--accent-yellow)"/>
      <circle cx="22" cy="19" r="4.5" fill="var(--bg-deep)"/>
      <path d="M20 21 L18.5 31 H25.5 L24 21 Z" fill="var(--bg-deep)"/>
    </svg>
    <span class="service__label">ΚΛΕΙΔΑΡΙΕΣ ΑΣΦΑΛΕΙΑΣ</span>
  </div>
</div>
</body>
</html>
```